Business Card + Stationery Design for a Craft Beer Bar

Mr. Tovell's is a taproom sport bar that contains in its menu beers from different places around the world. What we offer differently is the experience that you can get inside our location, ambient music with rock from the 80s to 90s, projection with the sports of the moment, board games and private events.

Target Market(s)

Young people, Mid and High Class

Industry/Entity Type

Business

Font styles to use
Serif
Sans Serif

Colors
fee18a

Requirements
Must have
• Name, Title, Contact Details, Website
Nice to have
• Mail Signature
Should not have
• n/a

```html
<!DOCTYPE html>
<html lang="en">
<head>
<meta charset="utf-8">
<title>Mr. Tovell's – Business Card</title>
<link rel="stylesheet" href="https://fonts.googleapis.com/css2?family=Source+Sans+3:wght@400;700&display=swap">
<style>
  :root {
    --card-yellow: #f5c662;
    --line-cream: #fde4a8;
    --frame-cream: #f8dc9c;
    --ink: #141414;
  }
  * { margin: 0; padding: 0; box-sizing: border-box; }
  html, body {
    width: 1200px;
    height: 750px;
    overflow: hidden;
    background: var(--card-yellow);
  }
  .card {
    position: relative;
    width: 1200px;
    height: 750px;
    background: var(--card-yellow);
    font-family: "Source Sans 3", sans-serif;
    color: var(--ink);
    overflow: hidden;
  }
  .card__arcs {
    position: absolute;
    inset: 0;
  }
  .card__frame {
    position: absolute;
    left: 47px;
    top: 47px;
    width: 1106px;
    height: 655px;
    border: 2px solid var(--frame-cream);
    box-shadow: 1px 1px 2px rgba(150, 110, 30, 0.25);
  }
  .brand {
    position: absolute;
    left: 0;
    width: 1200px;
    top: 110px;
    display: flex;
    flex-direction: column;
    align-items: center;
  }
  .brand__dot {
    width: 38px;
    height: 38px;
    border-radius: 50%;
    background: var(--ink);
  }
  .brand__name {
    margin-top: 77px;
    font-weight: 700;
    font-size: 50px;
    letter-spacing: 2px;
    line-height: 1;
    text-transform: uppercase;
  }
  .person {
    position: absolute;
    left: 77px;
    width: 400px;
    top: 420px;
    text-align: center;
  }
  .person__name {
    font-weight: 700;
    font-size: 50px;
    line-height: 1.2;
    text-transform: uppercase;
  }
  .person__title {
    font-weight: 400;
    font-size: 38px;
    line-height: 1.2;
    margin-top: 2px;
    text-transform: uppercase;
  }
  .contact {
    position: absolute;
    left: 651px;
    top: 420px;
    list-style: none;
    font-size: 38px;
    line-height: 51px;
    font-weight: 400;
    white-space: nowrap;
  }
</style>
</head>
<body>
  <div class="card">
    <svg class="card__arcs" width="1200" height="750" viewBox="0 0 1200 750" aria-hidden="true">
      <g fill="none" stroke="var(--line-cream)" stroke-width="3">
        <circle cx="1213" cy="-13" r="286"/>
        <circle cx="1213" cy="-13" r="262"/>
        <circle cx="-25" cy="762" r="292"/>
        <circle cx="-25" cy="762" r="266"/>
      </g>
    </svg>

    <div class="card__frame"></div>

    <div class="brand">
      <span class="brand__dot"></span>
      <span class="brand__name">Mr. Tovell's</span>
    </div>

    <div class="person">
      <p class="person__name">Dana Marlow</p>
      <p class="person__title">Owner</p>
    </div>

    <ul class="contact">
      <li>Your Address</li>
      <li>City, State, Zip</li>
      <li>Phone: 555-014-2087</li>
      <li>Email: dana@mrtovells.com</li>
      <li>Website: www.mrtovells.com</li>
    </ul>
  </div>
</body>
</html>
```